Workout book cover design: Looking for Simple Classic Cover

I need a book cover design for "The Steady Middle". A book on exercises to strengthen the pelvic floor. Basically it's exercises for your torso and hips. I want something tasteful and classic looking.

I like this book cover design: http://www.pagelorn-books.example/Calm-Starters-Gentle-Routines-Ease-ebook/dp/Q93KX7TM41/ref=sr_1_40?ie=UTF8&qid=2958173306&sr=8-40&keywords=exercise+books

Book Title: The Steady Middle
Description to go under title: I'm working on that now and will have ready by the end of the project. (The hidden world of pelvic floor training. Discover the best exercises for creating a strong core, hips and pelvis today!)

Target Market(s)

Mostly women 35-65 and men 60+

Industry/Entity Type

Health And Wellness

Requirements
Must have
• ebook dementions: 1536 x 2048 I think works for all the online publishing companies
• 8x10 for print
Nice to have
• I like this book cover design: http://www.pagelorn-books.example/Calm-Starters-Gentle-Routines-Ease-ebook/dp/Q93KX7TM41/ref=sr_1_40?ie=UTF8&qid=2958173306&sr=8-40&keywords=exercise+books
• This cover is also ok, but no shiny. http://www.pagelorn-books.example/Bedrock-Renew-The-Climb-Poise/dp/4827305519/ref=sr_1_2?ie=UTF8&qid=2958176642&sr=8-2&keywords=foundation+book
Should not have
• I do not like this cover, it's crowded. http://www.pagelorn-books.example/Gym-Drills-Selfweight-flexing-drills-ebook/dp/Q71RWJZNHE/ref=sr_1_2?ie=UTF8&qid=2958174418&sr=8-2&keywords=workout+books
• I do not want anyone on the cover making eye contact.

```html
<!DOCTYPE html>
<html lang="en">
<head>
<meta charset="utf-8">
<title>The Steady Middle — Book Cover</title>
<link href="https://fonts.googleapis.com/css2?family=Antonio:wght@100;200&family=Josefin+Sans:wght@300&family=Libre+Baskerville:ital@0;1&family=Montserrat:wght@600&display=swap" rel="stylesheet">
<style>
  :root {
    --backdrop: #e9e8e4;
    --paper: #fbf8e8;
    --rose: #c4686c;
    --ink-soft: #8a8884;
    --ink-light: #b3b1ab;
    --aqua: #5fe0dc;
    --aqua-band: #74e8e0;
    --white: #ffffff;
  }
  * { margin: 0; padding: 0; box-sizing: border-box; }
  html, body {
    width: 1200px; height: 1200px; overflow: hidden;
    background: var(--backdrop);
  }
  .cover {
    position: absolute; left: 188px; top: 50px;
    width: 825px; height: 1100px;
    background: var(--paper);
    overflow: hidden;
    box-shadow: 0 10px 30px rgba(0,0,0,.12);
    text-align: center;
  }
  .cover__kicker {
    margin: 42px auto 0; width: 640px;
    font-family: "Montserrat", sans-serif; font-weight: 600;
    font-size: 23px; letter-spacing: 3px; line-height: 1.15;
    color: var(--rose); text-transform: uppercase;
  }
  .cover__blurb {
    margin: 6px auto 0; width: 640px;
    font-family: "Josefin Sans", sans-serif; font-weight: 300;
    font-size: 16px; line-height: 1.3; color: var(--ink-soft);
    text-transform: uppercase;
  }
  .cover__pretitle {
    margin-top: 26px;
    font-family: "Josefin Sans", sans-serif; font-weight: 300;
    font-size: 50px; letter-spacing: 18px; padding-left: 18px;
    color: var(--ink-light); line-height: 1;
  }
  .cover__title {
    margin-top: 6px;
    font-family: "Antonio", sans-serif; font-weight: 100;
    font-size: 210px; line-height: .95; letter-spacing: 6px;
    color: var(--aqua); text-transform: uppercase;
  }
  .cover__subtitle {
    margin-top: 16px;
    font-family: "Libre Baskerville", serif; font-style: italic;
    font-size: 27px; color: var(--ink-soft);
  }
  .cover__tagline {
    margin-top: 6px;
    font-family: "Libre Baskerville", serif; font-style: italic;
    font-size: 16px; color: var(--ink-soft);
  }
  .cover__divider { display: block; margin: 18px auto 0; }
  .cover__photo {
    position: absolute; left: 0; right: 0; top: 640px; bottom: 70px;
    background:
      linear-gradient(180deg, var(--paper) 0%, rgba(251,248,232,0) 28%),
      linear-gradient(180deg, #f1d9c6 20%, #d9b3aa 45%, #a8a39f 70%, #7f9a98 100%);
  }
  .cover__band {
    position: absolute; left: 0; right: 0; bottom: 0; height: 70px;
    background: var(--aqua-band);
    display: flex; align-items: center; justify-content: center;
  }
  .cover__author {
    font-family: "Libre Baskerville", serif; font-size: 18px;
    letter-spacing: 4px; color: var(--white); text-transform: uppercase;
  }
</style>
</head>
<body>
  <main class="cover">
    <p class="cover__kicker">The perfect pelvic floor training for men and women</p>
    <p class="cover__blurb">The exercises are gentle and safe. They're also fun to do and easy to fit into your daily routine, and the success is immediate.</p>
    <h1>
      <span class="cover__pretitle" style="display:block">THE STEADY</span>
      <span class="cover__title" style="display:block">Middle</span>
    </h1>
    <p class="cover__subtitle">The hidden world of pelvic floor training.</p>
    <p class="cover__tagline">Discover the best exercises for creating a strong core, hips and pelvis today!</p>
    <svg class="cover__divider" width="18" height="18" viewBox="0 0 18 18" aria-hidden="true">
      <rect x="4" y="4" width="10" height="10" fill="#c9c7c1" transform="rotate(45 9 9)"/>
    </svg>
    <div class="cover__photo" role="img" aria-label="Photo of a woman in running gear jogging up wide outdoor stairs, seen from behind, in soft warm morning haze"></div>
    <footer class="cover__band">
      <span class="cover__author">Book Author</span>
    </footer>
  </main>
</body>
</html>
```